Startup photography business has a new logo, now we need business cards

Design a business card for the two partners of our business.
Our business Brisk Pelican has a new logo and we need to design a business card to showcase it and us.
Our colours of blue and orange are punchy and vivid, but how can we make the most of it on our card?

It should have our name Brisk Pelican
name of partner
phone number
email
website

Industry/Entity Type

Professional Photography

Contact Information for Business Card

Tom Ashworth
+61 400 55 61 72
tom@briskpelican.com.au
briskpelican.com.au

second card
Neil Porter
+61 400 918 263
neil@briskpelican.com.au
briskpelican.com.au

Colors
f37122
f68d4c
33a6d7
0592cd

Requirements
Must have
• one version of our logo, we have included options
• Name
• phone number
• email
• website
Nice to have
• instagram briskpelicanmedia
• twitter briskpelicanmedia
• facebook briskpelicanmedia

```html
<!DOCTYPE html>
<html lang="en">
<head>
<meta charset="utf-8">
<title>Brisk Pelican – Business Cards</title>
<link rel="stylesheet" href="https://fonts.googleapis.com/css2?family=Tinos:wght@400;700&display=swap">
<style>
  :root {
    --page-bg: #e6e6e8;
    --blue: #33a6d7;
    --blue-deep: #0592cd;
    --blue-bright: #22bdee;
    --orange: #f37122;
    --orange-soft: #f68d4c;
    --cream: #fcf7cb;
    --peach: #fbe0b6;
    --white: #ffffff;
  }
  * { margin: 0; padding: 0; box-sizing: border-box; }
  html, body { width: 1200px; height: 800px; overflow: hidden; }
  body {
    background: var(--page-bg);
    font-family: "Tinos", "Times New Roman", serif;
    position: relative;
  }
  .card {
    position: absolute;
    width: 520px;
    height: 300px;
    border-radius: 4px;
    overflow: hidden;
    box-shadow: 0 10px 24px rgba(0,0,0,0.18);
  }
  .card--front {
    left: 50px;
    top: 150px;
    background: linear-gradient(135deg, var(--blue-bright) 0%, var(--blue-bright) 45%, var(--blue-deep) 100%);
    display: flex;
    align-items: center;
    justify-content: center;
  }
  .card--back {
    left: 630px;
    top: 350px;
    background: var(--cream);
  }
  .brand {
    display: flex;
    align-items: center;
    gap: 14px;
    font-weight: 700;
    letter-spacing: 0.5px;
    white-space: nowrap;
  }
  .brand__dot {
    border-radius: 50%;
    flex: none;
  }
  .card--front .brand { color: var(--white); font-size: 46px; }
  .card--front .brand__dot { width: 58px; height: 58px; border: 6px solid var(--white); }
  .card--back .brand {
    position: absolute;
    left: 34px;
    bottom: 52px;
    color: var(--blue);
    font-size: 30px;
  }
  .card--back .brand__dot { width: 40px; height: 40px; border: 5px solid var(--orange); }
  .backdrop-mark {
    position: absolute;
    right: -70px;
    top: -40px;
    width: 320px;
    height: 320px;
    border-radius: 50%;
    background: var(--peach);
    opacity: 0.75;
  }
  .contact {
    position: absolute;
    right: 26px;
    top: 46px;
    color: var(--blue);
    font-size: 17px;
    line-height: 1.45;
    text-align: left;
  }
  .contact__name { font-size: 22px; margin-bottom: 4px; }
  .contact__social {
    display: flex;
    align-items: center;
    gap: 8px;
    margin-top: 10px;
  }
  .contact__social-dot {
    width: 22px;
    height: 22px;
    border-radius: 50%;
    background: var(--blue);
    flex: none;
  }
</style>
</head>
<body>
  <section class="card card--front" aria-label="Business card front">
    <div class="brand">
      <span class="brand__dot"></span>
      <span class="brand__name">Brisk Pelican</span>
    </div>
  </section>

  <section class="card card--back" aria-label="Business card back">
    <div class="backdrop-mark" role="img" aria-label="Faint brand mark decoration"></div>
    <div class="brand">
      <span class="brand__dot"></span>
      <span class="brand__name">Brisk Pelican</span>
    </div>
    <address class="contact" style="font-style: normal;">
      <div class="contact__name">Neil Porter</div>
      <div class="contact__phone">+61 400 918 263</div>
      <div class="contact__email">neil@briskpelican.com.au</div>
      <div class="contact__web">briskpelican.com.au</div>
      <div class="contact__social">
        <span class="contact__social-dot"></span>
        <span>briskpelicanmedia</span>
      </div>
    </address>
  </section>
</body>
</html>
```